Cat Litter Package and Logo Design

We want new package and Logo design for Cat pine wood litter. Name is “OLVO”. It will be sold in pet store, online shop and supermarket. Our slogan is “Cat litter for your cat, the member of our family”. I mean that cat is not just a pet. They like people in our family. The product for cat is must be the best as selected for member of our family.

Package: Plastic bag with 2 sides
Package Dimension: width 35 cm height 50 cm

Important:
1. Customer will know immediately what product is and for.
2. Outstanding from competitors.
3. Easy to recognize the product.

Front side detail:
1. Cat image
2. Logo: Olvo
3. Slogan: Cat litter for your cat, the member of our family.
4. Detail: Pine Wood Cat Litter
5. Main Highlight -> Breeder Selected
6. Main Features -> Non-Clumping / Odor Control / Dust Free / Save Money / Eco Friendly
7. Show real product (pine wood) inside package: Area to show product will be transparent.
8. Net WT 10 L

Back side detail:
1. One bag for 1 cat & 2 months
2. Benefit: Non-Clumping / Odor Control / Dust Free / Save Money / Eco Friendly
3. How to change for using Olvo Pine Wood Litter: Please mix Olvo with the old one. When your cat can be familiar with Olvo. You can use only Olvo in your cat litter tray.
4. Direction
4.1 Fill the litter height for 2 inches.
4.2 Scoop solid waste.
4.3 Shake litter tray for urine sawdust
4.4 Maintain the height of litter for 2 inches.
5. Imported and Distribution by
5.1 QFO Tech Co.,Ltd.
5.2 Email: Quietfernowlstudio@plumbox.net
6. Little text: *Recommended to use with cat litter tray.

Attached:
1. Our competitors packages
2. Real Cat: You can use it on the package. (I have attached many images, you can select it and use for suitable way.)***
3. Cat litter tray: Don’t use this image. It’s just for describe what is cat litter tray. I prefer drawing.
4. Real product: pine wood

Note: Cat litter is for cat toilet. It's not cat's food.

Target Market(s)

Cat owners whose cats use a litter tray

Industry/Entity Type

Pet

Logo Text

OLVO

Requirements
Must have
• 1. Customer will know immediately what product is and for.
• 2. Outstanding from competitors.
• 3. Easy to recognize the product.

```html
<!DOCTYPE html>
<html lang="en">
<head>
<meta charset="UTF-8">
<title>OLVO Pine Wood Cat Litter – Package Fronts</title>
<link rel="stylesheet" href="https://fonts.googleapis.com/css2?family=Oswald:wght@300;400&family=Caveat:wght@400&family=Cinzel:wght@600&family=Courier+Prime:wght@700&family=Lato:wght@400&display=swap">
<style>
  :root {
    --stage: #666666;
    --dark-top: #2e2e2e;
    --dark-bottom: #111111;
    --paper: #ffffff;
    --leaf: #8cc63f;
    --crimson: #9b1b1f;
    --orchid: #d57fc1;
    --bark: #7a3b12;
    --peach: #e9b48e;
    --berry: #a01c1f;
    --ink-dark: #1f1f1f;
    --pellet-light: #e6c49c;
    --pellet-dark: #b98a58;
  }
  * { margin: 0; padding: 0; box-sizing: border-box; }
  html, body { width: 1200px; height: 790px; overflow: hidden; background: var(--stage); }
  .canvas { position: relative; width: 1200px; height: 790px; }
  .bag { position: absolute; top: 158px; width: 330px; height: 478px; }
  .bag--night { left: 190px; }
  .bag--day { left: 692px; }
  .bag svg { display: block; width: 100%; height: 100%; }

  .wordmark { font-family: 'Oswald', sans-serif; font-weight: 400; font-size: 62px; letter-spacing: 1px; }
  .slogan { font-family: 'Caveat', cursive; font-size: 11px; }
  .highlight { font-family: 'Oswald', sans-serif; font-weight: 300; font-size: 16px; fill: var(--paper); }
  .highlight--night { font-size: 24px; }
  .feature-ring { font-family: 'Lato', sans-serif; font-size: 6px; }
  .feature-main { font-family: 'Courier Prime', monospace; font-weight: 700; font-size: 8.5px; }
  .product-name { font-family: 'Cinzel', serif; font-weight: 600; font-size: 16px; letter-spacing: 1px; }
  .net-weight { font-family: 'Oswald', sans-serif; font-weight: 400; font-size: 9.5px; }
</style>
</head>
<body>
<main class="canvas">

  <!-- Dark edition -->
  <section class="bag bag--night">
    <svg viewBox="0 0 330 478" xmlns="http://www.w3.org/2000/svg">
      <defs>
        <linearGradient id="night-fill" x1="0" y1="0" x2="0" y2="1">
          <stop offset="0" stop-color="var(--dark-top)"/>
          <stop offset="1" stop-color="var(--dark-bottom)"/>
        </linearGradient>
        <radialGradient id="pellet-fill" cx="0.45" cy="0.45" r="0.6">
          <stop offset="0" stop-color="var(--pellet-light)"/>
          <stop offset="1" stop-color="var(--pellet-dark)"/>
        </radialGradient>
        <linearGradient id="cat-fill" x1="0" y1="0" x2="0" y2="1">
          <stop offset="0" stop-color="#c99a62"/>
          <stop offset="0.5" stop-color="#e8d7b4"/>
          <stop offset="1" stop-color="#a98358"/>
        </linearGradient>
        <path id="night-arc-top" d="M 24 296 Q 90 236 156 284"/>
        <path id="night-arc-low" d="M 40 316 Q 92 272 140 314"/>
        <path id="night-ring-top" d="M 225.9 103.1 A 32 32 0 0 1 286.1 103.1"/>
        <path id="night-ring-low" d="M 222.2 126.3 A 36 36 0 0 0 289.8 126.3"/>
      </defs>

      <rect class="bag-body" width="330" height="478" fill="url(#night-fill)"/>
      <line class="seal-line" x1="18" y1="28" x2="292" y2="28" stroke="#8a8a8a" stroke-width="1"/>

      <text class="wordmark" x="22" y="103" fill="var(--leaf)">OLVO</text>
      <text class="slogan" x="30" y="116" fill="#cfcfcf" textLength="178" lengthAdjust="spacingAndGlyphs">Cat litter for your cat, the member of our family</text>

      <g class="feature-badge">
        <circle cx="256" cy="114" r="41" fill="none" stroke="var(--paper)" stroke-width="1.6"/>
        <circle cx="256" cy="114" r="38" fill="none" stroke="var(--paper)" stroke-width="0.9" stroke-dasharray="1.5 2"/>
        <text class="feature-ring" fill="var(--paper)"><textPath href="#night-ring-top" startOffset="50%" text-anchor="middle">Odor Control • Dust Free</textPath></text>
        <text class="feature-main" x="256" y="117" text-anchor="middle" fill="var(--paper)">Non-Clumping</text>
        <text class="feature-ring" fill="var(--paper)"><textPath href="#night-ring-low" startOffset="50%" text-anchor="middle">Save Money • Eco Friendly</textPath></text>
      </g>

      <rect class="highlight-band" x="-4" y="152" width="136" height="24" fill="var(--crimson)"/>
      <text class="highlight highlight--night" x="26" y="172" textLength="174" lengthAdjust="spacing">Breeder Selected</text>

      <rect class="cat-photo" x="146" y="186" width="132" height="280" rx="40" fill="url(#cat-fill)" opacity="0.9" role="img" aria-label="Photo of a seated tabby and white cat with an orange ball"/>

      <text class="product-name" fill="var(--peach)"><textPath href="#night-arc-top" startOffset="50%" text-anchor="middle">PINE WOOD</textPath></text>
      <text class="product-name" fill="var(--peach)"><textPath href="#night-arc-low" startOffset="50%" text-anchor="middle">CAT LITTER</textPath></text>

      <circle class="product-window" cx="94" cy="364" r="61" fill="url(#pellet-fill)" role="img" aria-label="Transparent window showing pine wood pellets"/>

      <rect class="ground-band" x="0" y="454" width="330" height="24" fill="var(--leaf)"/>
      <path class="net-tab" d="M 122 478 L 122 446 Q 122 430 154 430 Q 186 430 186 446 L 186 478 Z" fill="var(--leaf)" stroke="var(--ink-dark)" stroke-width="1.2"/>
      <text class="net-weight" x="154" y="452" text-anchor="middle" fill="var(--ink-dark)">Net WT 10L</text>
    </svg>
  </section>

  <!-- Light edition -->
  <section class="bag bag--day">
    <svg viewBox="0 0 330 478" xmlns="http://www.w3.org/2000/svg">
      <defs>
        <radialGradient id="pellet-fill-day" cx="0.45" cy="0.45" r="0.6">
          <stop offset="0" stop-color="var(--pellet-light)"/>
          <stop offset="1" stop-color="var(--pellet-dark)"/>
        </radialGradient>
        <linearGradient id="cat-fill-day" x1="0" y1="0" x2="0" y2="1">
          <stop offset="0" stop-color="#c99a62"/>
          <stop offset="0.5" stop-color="#ead9b6"/>
          <stop offset="1" stop-color="#a98358"/>
        </linearGradient>
        <path id="day-arc-top" d="M 24 296 Q 90 236 156 284"/>
        <path id="day-arc-low" d="M 40 316 Q 92 272 140 314"/>
        <path id="day-ring-top" d="M 199.9 81.1 A 32 32 0 0 1 260.1 81.1"/>
        <path id="day-ring-low" d="M 196.2 104.3 A 36 36 0 0 0 263.8 104.3"/>
      </defs>

      <rect class="bag-body" width="330" height="478" fill="var(--paper)"/>

      <rect class="highlight-band" x="8" y="40" width="134" height="24" fill="var(--orchid)"/>
      <text class="highlight" x="22" y="58" textLength="114" lengthAdjust="spacing">Breeder Selected</text>

      <text class="wordmark" x="14" y="146" fill="var(--bark)">OLVO</text>
      <text class="slogan" x="20" y="162" fill="#333333" textLength="178" lengthAdjust="spacingAndGlyphs">Cat litter for your cat, the member of our family</text>

      <g class="feature-badge">
        <circle cx="230" cy="92" r="41" fill="none" stroke="var(--bark)" stroke-width="1.6"/>
        <circle cx="230" cy="92" r="38" fill="none" stroke="var(--bark)" stroke-width="0.9" stroke-dasharray="1.5 2"/>
        <text class="feature-ring" fill="var(--bark)"><textPath href="#day-ring-top" startOffset="50%" text-anchor="middle">Odor Control • Dust Free</textPath></text>
        <text class="feature-main" x="230" y="95" text-anchor="middle" fill="var(--bark)">Non-Clumping</text>
        <text class="feature-ring" fill="var(--bark)"><textPath href="#day-ring-low" startOffset="50%" text-anchor="middle">Save Money • Eco Friendly</textPath></text>
      </g>

      <rect class="cat-photo" x="150" y="190" width="134" height="278" rx="40" fill="url(#cat-fill-day)" opacity="0.9" role="img" aria-label="Photo of a seated tabby and white cat with an orange ball"/>

      <text class="product-name" fill="var(--berry)"><textPath href="#day-arc-top" startOffset="50%" text-anchor="middle">PINE WOOD</textPath></text>
      <text class="product-name" fill="var(--berry)"><textPath href="#day-arc-low" startOffset="50%" text-anchor="middle">CAT LITTER</textPath></text>

      <circle class="product-window" cx="92" cy="364" r="61" fill="url(#pellet-fill-day)" role="img" aria-label="Transparent window showing pine wood pellets"/>

      <rect class="ground-band" x="0" y="454" width="330" height="24" fill="var(--leaf)"/>
      <path class="net-tab" d="M 126 478 L 126 446 Q 126 430 158 430 Q 190 430 190 446 L 190 478 Z" fill="var(--leaf)" stroke="var(--paper)" stroke-width="1.2"/>
      <text class="net-weight" x="158" y="452" text-anchor="middle" fill="var(--paper)">Net WT 10L</text>
    </svg>
  </section>

</main>
</body>
</html>
```